Tarvell homes and renovations business card design.

Would like some new card designs utilizing my new logo that look professional. I am open to different colors on the logo or utilize the same ones we have. I like the original concept but would like to see some fresh ideas and build on what we have already done.

Target Market(s)

Custom home building industry, Real estate sales, Renovation projects.

Industry/Entity Type

Home Builder

Contact Information for Business Card

Tarvell Homes and Renovations
2871 162nd Street
Frank, Alberta
T0L3P0
Home : 403- 555-0187 Cell: 403- 555-0243

My info is : Gus Tarvell, President and CEO
email: tarvellhomes@quillmail.example
Website: tarvellhomes.example

Requirements
Must have
• Must Use my new logo design. I am open to different colors on the logo or utilize the same ones in the existing design. I can upload the original logo design if needed.

```html
<!DOCTYPE html>
<html lang="en">
<head>
<meta charset="utf-8">
<title>Tarvell Homes and Renovations – Business Cards</title>
<link href="https://fonts.googleapis.com/css2?family=Fjalla+One&family=Arimo:wght@400;600&display=swap" rel="stylesheet">
<style>
  :root {
    --backdrop: #ececec;
    --card-yellow: #f7bb22;
    --card-charcoal: #363334;
    --ink-dark: #3b3b3d;
    --ink-soft: #4a4236;
    --paper-white: #ffffff;
    --band-edge: #e4e4e4;
  }
  * { margin: 0; padding: 0; box-sizing: border-box; }
  html, body {
    width: 1200px;
    height: 1007px;
    overflow: hidden;
    background: var(--backdrop);
  }
  .canvas {
    position: relative;
    width: 1200px;
    height: 1007px;
  }
  .card {
    position: absolute;
    width: 622px;
    height: 352px;
    box-shadow: 0 2px 6px rgba(0,0,0,0.18);
  }

  /* Front card */
  .card--front {
    left: 287px;
    top: 88px;
    background: var(--card-yellow);
  }
  .brand-tab {
    position: absolute;
    left: -7px;
    top: 152px;
    width: 145px;
    height: 80px;
    background: var(--paper-white);
    display: flex;
    align-items: center;
    justify-content: center;
    box-shadow: 0 1px 3px rgba(0,0,0,0.15);
  }
  .brand-tab .company-name {
    font-family: "Arimo", sans-serif;
    font-weight: 400;
    color: var(--ink-dark);
    font-size: 9px;
    white-space: nowrap;
  }
  .contact {
    position: absolute;
    left: 166px;
    top: 74px;
    font-family: "Arimo", sans-serif;
    color: var(--ink-soft);
    font-size: 13.5px;
    line-height: 1.45;
  }
  .contact .holder {
    font-family: "Fjalla One", sans-serif;
    font-weight: 400;
    font-size: 20px;
    color: var(--ink-dark);
    text-transform: uppercase;
    letter-spacing: 0.3px;
    margin-bottom: 8px;
  }
  .contact .online p { margin-bottom: 4px; }
  .contact .postal { margin-top: 16px; margin-left: 6px; font-style: normal; }

  /* Back card */
  .card--back {
    left: 290px;
    top: 562px;
    background: var(--card-charcoal);
  }
  .company-line {
    position: absolute;
    left: 50px;
    top: 146px;
    display: flex;
    align-items: center;
    gap: 8px;
  }
  .company-line .marker {
    width: 10px;
    height: 10px;
    background: var(--paper-white);
  }
  .company-line .company-name {
    font-family: "Arimo", sans-serif;
    font-weight: 400;
    color: var(--paper-white);
    font-size: 14px;
    white-space: nowrap;
  }
  .name-band {
    position: absolute;
    left: 300px;
    top: 126px;
    width: 322px;
    height: 58px;
    background: linear-gradient(180deg, #ffffff 0%, #f1f1f1 100%);
    box-shadow: 0 2px 4px rgba(0,0,0,0.3);
    padding: 10px 0 0 18px;
  }
  .name-band::after {
    content: "";
    position: absolute;
    right: 0;
    top: 0;
    width: 12px;
    height: 100%;
    background: var(--band-edge);
  }
  .name-band .holder {
    font-family: "Fjalla One", sans-serif;
    font-weight: 400;
    font-size: 22px;
    color: #1e1e1e;
    text-transform: uppercase;
    line-height: 1;
  }
  .name-band .role {
    font-family: "Arimo", sans-serif;
    font-size: 13px;
    color: #3a3a3a;
    margin-top: 2px;
  }
</style>
</head>
<body>
<main class="canvas">
  <section class="card card--front" aria-label="Business card front">
    <div class="brand-tab">
      <span class="company-name">Tarvell Homes and Renovations</span>
    </div>
    <div class="contact">
      <h1 class="holder">Gus Tarvell. President and CEO</h1>
      <div class="online">
        <p>tarvellhomes@quillmail.example</p>
        <p>tarvellhomes.example</p>
      </div>
      <address class="postal">
        2871 162nd Street<br>
        Frank, Alberta, T0L3P0<br>
        Home : 403- 555-0187&nbsp; Cell: 403- 555-0243
      </address>
    </div>
  </section>

  <section class="card card--back" aria-label="Business card back">
    <div class="company-line">
      <span class="marker"></span>
      <span class="company-name">Tarvell Homes and Renovations</span>
    </div>
    <div class="name-band">
      <h2 class="holder">Gus Tarvell</h2>
      <p class="role">President and CEO</p>
    </div>
  </section>
</main>
</body>
</html>
```